Quelvon Corporate General Presentation

Quelvon is a leading player in ICT (Information Communication Technology) cooling, we need a design for our corporate general presentation.

Attached is a reference of content

Our logo main color is industrial blue, our technology is green (energy saving).

existing website: www.quel-von.com www.quel-von.uk

Target Market(s)

Global

Industry/Entity Type

Communication

Number of Pages Required

5+ page

Font styles to use
Serif
Sans Serif

Colors
0255a3
3176b5
0293ce
33a6d7
9bcb3c

```html
<!DOCTYPE html>
<html lang="en">
<head>
<meta charset="utf-8">
<title>Quelvon – Our Core Values</title>
<link href="https://fonts.googleapis.com/css2?family=Lato:wght@400;700&display=swap" rel="stylesheet">
<style>
  :root {
    --bg: #ffffff;
    --title: #8c9196;
    --subtitle: #9a9ea3;
    --accent: #05a7ec;
    --heading: #1b8fd2;
    --body: #8f9397;
    --icon-fg: #ffffff;
  }
  * { margin: 0; padding: 0; box-sizing: border-box; }
  html, body { width: 1200px; height: 675px; overflow: hidden; background: var(--bg); }
  body { font-family: "Lato", Arial, sans-serif; }

  .slide { position: relative; width: 1200px; height: 675px; background: var(--bg); }

  .slide-header { position: absolute; top: 46px; left: 0; width: 100%; text-align: center; }
  .slide-title { font-size: 33px; font-weight: 400; color: var(--title); letter-spacing: 0.2px; line-height: 1.1; }
  .slide-subtitle { margin-top: 4px; font-size: 15px; color: var(--subtitle); }

  .value { position: absolute; width: 520px; }
  .value-icon { position: absolute; width: 98px; height: 98px; }
  .value-icon svg { width: 100%; height: 100%; display: block; }
  .value-text { position: absolute; width: 370px; }
  .value-name { font-size: 18px; font-weight: 400; color: var(--heading); letter-spacing: 0.3px; line-height: 1; }
  .value-desc { margin-top: 12px; font-size: 15.6px; line-height: 21.7px; color: var(--body); }

  .value--reliable    { left: 46px;  top: 206px; }
  .value--responsible { left: 621px; top: 198px; }
  .value--efficient   { left: 46px;  top: 400px; }
  .value--respectful  { left: 621px; top: 414px; }

  .value--reliable .value-icon    { left: 0; top: 8px; }
  .value--responsible .value-icon { left: 0; top: 0; }
  .value--efficient .value-icon   { left: 0; top: 0; }
  .value--respectful .value-icon  { left: 0; top: 0; }

  .value--reliable .value-text    { left: 162px; top: 0; }
  .value--responsible .value-text { left: 126px; top: 8px; }
  .value--efficient .value-text   { left: 162px; top: 20px; }
  .value--respectful .value-text  { left: 126px; top: 6px; }
</style>
</head>
<body>
<main class="slide">
  <header class="slide-header">
    <h1 class="slide-title">Our Core Values</h1>
    <p class="slide-subtitle">Write here a great subtitle</p>
  </header>

  <section class="value value--reliable">
    <div class="value-icon">
      <svg viewBox="0 0 100 100" aria-hidden="true">
        <circle cx="50" cy="50" r="49" fill="var(--accent)"/>
        <path d="M30 51 L44 65 L71 36" fill="none" stroke="var(--icon-fg)" stroke-width="8" stroke-linecap="round" stroke-linejoin="round"/>
      </svg>
    </div>
    <div class="value-text">
      <h2 class="value-name">RELIABLE</h2>
      <p class="value-desc">Reliable means supplying reliable products and services and winning long-term trust from satisfied clients customers in order to maintain &amp; grow market share</p>
    </div>
  </section>

  <section class="value value--responsible">
    <div class="value-icon">
      <svg viewBox="0 0 100 100" aria-hidden="true">
        <circle cx="50" cy="50" r="49" fill="var(--accent)"/>
        <path d="M30 66 a13 13 0 0 1 -1 -26 a17 17 0 0 1 33 -6 a13 13 0 0 1 10 32 z" fill="var(--icon-fg)"/>
        <rect x="47" y="40" width="6" height="14" fill="var(--accent)"/>
        <path d="M41 52 L59 52 L50 62 z" fill="var(--accent)"/>
      </svg>
    </div>
    <div class="value-text">
      <h2 class="value-name">RESPONSIBLE</h2>
      <p class="value-desc">Responsible means being responsible &amp; caring for customers shareholders, employees, suppliers, and society.</p>
    </div>
  </section>

  <section class="value value--efficient">
    <div class="value-icon">
      <svg viewBox="0 0 100 100" aria-hidden="true">
        <circle cx="50" cy="50" r="49" fill="var(--accent)"/>
        <g fill="var(--icon-fg)">
          <ellipse cx="50" cy="31" rx="21" ry="7"/>
          <path d="M29 36 q21 10 42 0 v9 q-21 10 -42 0 z"/>
          <path d="M29 50 q21 10 42 0 v9 q-21 10 -42 0 z"/>
          <path d="M29 64 q21 10 42 0 v5 q-21 13 -42 0 z"/>
        </g>
      </svg>
    </div>
    <div class="value-text">
      <h2 class="value-name">EFFICIENT</h2>
      <p class="value-desc">Efficient means optimizing our resources distribution &amp; maintaining a lean organisation to ensure sustainable business development and maximizing our customers profit margins</p>
    </div>
  </section>

  <section class="value value--respectful">
    <div class="value-icon">
      <svg viewBox="0 0 100 100" aria-hidden="true">
        <circle cx="50" cy="50" r="49" fill="var(--accent)"/>
        <path d="M50 24 L57.6 40.5 L75.7 42.6 L62.3 54.9 L65.9 72.7 L50 63.8 L34.1 72.7 L37.7 54.9 L24.3 42.6 L42.4 40.5 z" fill="var(--icon-fg)" stroke="var(--icon-fg)" stroke-width="3" stroke-linejoin="round"/>
      </svg>
    </div>
    <div class="value-text">
      <h2 class="value-name">RESPECTFUL</h2>
      <p class="value-desc">Respectful means showing respect to all stakeholders, whether they are customers, employees, shareholders, suppliers, partners or competitors.</p>
    </div>
  </section>
</main>
</body>
</html>
```